Tolnar Social Media Banner

The objective of this campaign is to end up with a Banner Add to post in the content of our social media.

We are Tolnar, a business that is going to modify all the grocery shopping mechanism with a simple device. It works the following way. Our device is a bar-code scanner. Once installed in your home, you would scan your groceries trough and it will automatically create your shopping list. Once you decide you have all the items, you just click the “buy” button and you’ll receive your groceries home whenever you have selected. This way is like being in the grocery shop but from home. You’ll find a long video and short video attached to the project.

The objective is to create a Banner Add that simulates the SHORT video with icons. The goal is for the viewer to understand what our device do just by looking at the banner. We have thought about diving the banner into three frames: Scan, Buy and Receive. Although that is what we think is most understandable, let us know if you think otherwise.

For the Scan frame the viewer should be able to see clearly the scanning process of any grocery through our device. I attached a picture of how our device looks like. You could also look for more images googling “Tolnar”.

For the Buy frame there should be a mobile phone. The idea is that the viewer is able to recognize that the Buying process is through an App in your phone. The frame could be only a phone, it could also be a phone with the Tolnar app opened or even a phone with a “Buy” button. Further ideas for this icon will be more than welcome.

The Receive frame should be the easiest one of them all. It should be more than clear the meaning of the frame.

Between the frames, you could add some to enable to understand the whole process. There could be numbers (Example: 1. Scan, 2. Buy, 3. Receive), there could be a plus sign (Example: Scan + Buy = Receive), or there could also be arrows following the process. Again, ideas to this matter will be more than welcome.

Thank you and contact us for questions or more info.

- Long video: https://www.vidmarsh.example/watch?v=Qa7rLmPzE2d

- Short Video: https://www.vidmarsh.example/watch?v=Hn3xBtYcW9k

- Tolnar Device Picture: https://www.findlo.example/search?q=tolnar&img=1#r=Pq4sTz8wLm2A

- Tolnar Logo: https://www.findlo.example/search?q=tolnar&img=1#r=Vd6kGh1nRs9B

- Tolnar App: https://www.findlo.example/search?q=tolnar+app&img=1#r=Jw2cYe5uXo7C

Industry/Entity Type

Business

Requirements
Must have
• Hi again. I just uploaded an example of what we are looking for. Open the file Tolnar_Expositor. We would like the designs to adjust to it. Although that's what we would like, we are open to new propositions.
• IMPORTANT:
• 1. We would like to change where it says scan. I've uploaded a picture called Captura. The idea is to draw the device SCANNING a product so that it is clear the function of the scan.
• 2. Dimensions of the composition. We would like more room for the Scan, Check and Receive compositions. That is going to be done reducing the blue space.
• 3. Bottom of the image. As you will see there is a pretty big grey space at the bottom of the image. The idea is to reduce it a little bit. The corner of the white line should be pretty close to the end of the image, or even touching.

```html
<!DOCTYPE html>
<html lang="en">
<head>
<meta charset="utf-8">
<title>Tolnar Social Media Banner</title>
<link rel="stylesheet" href="https://fonts.googleapis.com/css2?family=Dosis:wght@400;500;600;700&display=swap">
<style>
  :root {
    --orange: #f2582f;
    --orange-light: #f9825f;
    --white: #ffffff;
    --ink: #58585a;
    --ink-soft: #4a4a4a;
    --blue: #3ba7e0;
    --blue-soft: #8fcdf0;
    --green: #8cc63f;
    --yellow: #fdbe17;
    --device-top: #ece6dc;
    --device-bottom: #cfc6b8;
    --bag-tone: #7fbf4a;
  }
  * { margin: 0; padding: 0; box-sizing: border-box; }
  html, body { width: 1200px; height: 676px; overflow: hidden; background: var(--white); }
  .banner {
    position: relative;
    width: 1200px;
    height: 676px;
    overflow: hidden;
    font-family: "Dosis", sans-serif;
  }
  .backdrop { position: absolute; inset: 0; }

  .bag-art {
    position: absolute;
    left: 87px; top: 105px;
    width: 273px; height: 280px;
    border-radius: 14px;
    background: linear-gradient(90deg, var(--blue) 0%, var(--bag-tone) 30%, var(--bag-tone) 65%, var(--yellow) 80%, var(--orange) 100%);
    border: 10px solid var(--white);
    transform: rotate(4deg);
  }

  .device-art {
    position: absolute;
    left: 796px; top: 84px;
    width: 233px; height: 468px;
    border-radius: 6px;
    background: linear-gradient(180deg, var(--device-top), var(--device-bottom));
    box-shadow: 0 0 22px rgba(255,255,255,.6);
  }

  .headline {
    position: absolute;
    right: 418px; top: 98px;
    z-index: 2;
    text-align: right;
    color: var(--white);
    font-weight: 400;
    font-size: 44px;
    line-height: 53px;
    white-space: nowrap;
  }
  .headline .brand { font-weight: 700; font-size: 48px; }

  .step {
    position: absolute;
    z-index: 3;
    border-radius: 8px;
    color: var(--white);
    font-weight: 500;
    font-size: 27px;
    text-align: center;
  }
  .step-label { position: absolute; left: 0; right: 0; bottom: 10px; line-height: 1; }
  .step::before {
    content: "";
    position: absolute;
    top: -14px;
    border-bottom: 16px solid currentColor;
  }
  .step-scan { left: 676px; top: 298px; width: 155px; height: 155px; background: var(--blue); }
  .step-scan::before { right: 0; color: var(--blue); border-left: 26px solid transparent; }
  .step-check { left: 980px; top: 351px; width: 132px; height: 130px; background: var(--green); }
  .step-check::before { left: 0; color: var(--green); border-right: 26px solid transparent; }
  .step-receive { left: 786px; top: 502px; width: 118px; height: 116px; background: var(--yellow); }
  .step-receive::before { right: 0; color: var(--yellow); border-left: 26px solid transparent; }

  .scan-art {
    position: absolute;
    left: 14px; top: 12px;
    width: 127px; height: 100px;
    border-radius: 50%;
    background: radial-gradient(ellipse at 60% 45%, var(--blue-soft) 0%, rgba(143,205,240,.45) 45%, rgba(59,167,224,0) 72%);
  }
  .step-icon { position: absolute; left: 50%; transform: translateX(-50%); }
  .step-check .step-icon { top: 14px; }
  .step-receive .step-icon { top: 12px; }

  .footer-brand {
    position: absolute;
    left: 50px; top: 532px;
    color: var(--ink);
    font-weight: 500;
    font-size: 80px;
    letter-spacing: -1px;
    line-height: 1;
  }
  .footer-divider {
    position: absolute;
    left: 283px; top: 533px;
    width: 2px; height: 87px;
    background: #9a9a9a;
  }
  .contact { position: absolute; left: 310px; top: 543px; list-style: none; }
  .contact li {
    display: flex; align-items: center; gap: 14px;
    color: var(--ink-soft);
    font-size: 21px;
    height: 36px;
  }
  .contact svg { width: 24px; height: 24px; flex: none; }
</style>
</head>
<body>
<main class="banner">
  <svg class="backdrop" viewBox="0 0 1200 676" width="1200" height="676" aria-hidden="true">
    <rect width="1200" height="676" fill="var(--orange)"/>
    <polygon points="0,267 1200,470 1200,676 0,676" fill="var(--orange-light)"/>
    <polygon points="0,322 1200,494 1200,676 0,676" fill="var(--white)"/>
  </svg>

  <div class="bag-art" role="img" aria-label="Illustrated shopping bag made of coloured stripes"></div>

  <div class="device-art" role="img" aria-label="Photo of the Tolnar home scanning device"></div>

  <h1 class="headline"><span class="brand">tolnar</span> does your<br>grocery shopping<br>for you</h1>

  <div class="step step-scan">
    <div class="scan-art" role="img" aria-label="Illustration of a hand holding a product up to the scanner"></div>
    <span class="step-label">Scan</span>
  </div>

  <div class="step step-check">
    <svg class="step-icon" width="34" height="60" viewBox="0 0 34 60" aria-hidden="true">
      <rect x="1.5" y="1.5" width="31" height="57" rx="5" fill="none" stroke="#fff" stroke-width="3"/>
      <rect x="5" y="9" width="24" height="38" fill="#fff" opacity=".9"/>
      <circle cx="17" cy="24" r="4" fill="none" stroke="var(--green)" stroke-width="2"/>
      <line x1="9" y1="34" x2="25" y2="34" stroke="var(--green)" stroke-width="2"/>
      <line x1="9" y1="39" x2="25" y2="39" stroke="var(--green)" stroke-width="2"/>
      <circle cx="17" cy="53" r="2" fill="#fff"/>
    </svg>
    <span class="step-label">Check</span>
  </div>

  <div class="step step-receive">
    <svg class="step-icon" width="52" height="50" viewBox="0 0 52 50" aria-hidden="true">
      <polygon points="26,3 49,13 26,23 3,13" fill="#fff3c9"/>
      <polygon points="3,13 26,23 26,47 3,37" fill="#fff"/>
      <polygon points="49,13 26,23 26,47 49,37" fill="#ffe59a"/>
      <polygon points="14,8 37,18 37,26 33,24 33,20 10,10" fill="#f0a500"/>
    </svg>
    <span class="step-label">Receive</span>
  </div>

  <div class="footer-brand">tolnar</div>
  <div class="footer-divider"></div>
  <ul class="contact">
    <li>
      <svg viewBox="0 0 24 24" aria-hidden="true"><path d="M6.6 3.5l3 3-2 2.4a13 13 0 0 0 7.5 7.5l2.4-2 3 3-2.2 2.8C12 20 4 12 3.8 5.7z" fill="none" stroke="var(--yellow)" stroke-width="2" stroke-linejoin="round"/></svg>
      <span>+00 000 000 0000</span>
    </li>
    <li>
      <svg viewBox="0 0 24 24" aria-hidden="true"><rect x="2" y="5" width="20" height="14" fill="var(--yellow)"/><path d="M2 5l10 8 10-8" fill="none" stroke="#fff" stroke-width="1.6"/></svg>
      <span>info@tolnar.example</span>
    </li>
  </ul>
</main>
</body>
</html>
```